Technology Services Fleet Wrap

We provide IT and Network Management Services to small to medium sized businesses. We would like to have our website, phone number, logo, services listed. We have a business to wrap the car but we need the design file for him to print the vinyl. Included an example picture of something we like. The blue in our logo is a color we would like to keep. The logo can be all one color it does not have to have the tech background that is currently in it

Target Market(s)

Businesses

Industry/Entity Type

Information Technology

```html
<!DOCTYPE html>
<html lang="en">
<head>
<meta charset="utf-8">
<title>Brightwire Tech – Fleet Wrap Side Panel</title>
<link rel="stylesheet" href="https://fonts.googleapis.com/css2?family=Oswald:wght@400;500&display=swap">
<style>
  :root {
    --navy: #15184a;
    --deep-blue: #1e3f8f;
    --texture-blue: #2b5bb5;
    --brand-blue: #1f6fc5;
    --sky: #2fa3e6;
    --panel-light: #eef6fc;
    --panel-mist: #cfe4f4;
    --page: #ffffff;
  }
  html, body {
    margin: 0;
    width: 1200px;
    height: 1200px;
    overflow: hidden;
    background: var(--page);
  }
  .canvas {
    width: 1200px;
    height: 1200px;
    display: flex;
    align-items: center;
    justify-content: center;
  }
  .wrap-panel {
    width: 1100px;
    height: 460px;
    display: block;
  }
  .wrap-panel text { font-family: "Oswald", sans-serif; }
  .service-heading { fill: var(--sky); font-size: 22px; font-weight: 500; letter-spacing: 1px; }
  .service-item { fill: var(--navy); font-size: 17px; font-weight: 400; }
  .brand-name { fill: var(--brand-blue); font-size: 38px; font-weight: 400; letter-spacing: 2px; }
  .brand-ring { fill: none; stroke: var(--brand-blue); stroke-width: 6; }
  .phone { fill: #ffffff; font-size: 30px; font-weight: 400; letter-spacing: 2px; }
  .website { fill: #ffffff; font-size: 20px; font-weight: 500; letter-spacing: 1px; }
</style>
</head>
<body>
<main class="canvas">
  <svg class="wrap-panel" viewBox="0 0 1100 460" xmlns="http://www.w3.org/2000/svg">
    <defs>
      <linearGradient id="mist" x1="0" y1="0" x2="0" y2="1">
        <stop offset="0" stop-color="var(--panel-mist)"/>
        <stop offset="0.55" stop-color="var(--panel-light)"/>
        <stop offset="1" stop-color="#ffffff"/>
      </linearGradient>
      <linearGradient id="circuit-tone" x1="0" y1="0" x2="1" y2="1">
        <stop offset="0" stop-color="var(--texture-blue)"/>
        <stop offset="1" stop-color="var(--deep-blue)"/>
      </linearGradient>
    </defs>

    <!-- light centre panel -->
    <rect class="centre-panel" x="0" y="0" width="1100" height="460" fill="url(#mist)"/>

    <!-- left tech texture field with chevron -->
    <polygon class="texture-left" role="img" aria-label="Blue circuit-board texture"
      points="0,0 300,0 250,230 310,460 0,460" fill="url(#circuit-tone)"/>
    <polygon class="stripe-navy" points="196,140 214,140 281,460 263,460" fill="var(--navy)"/>
    <polygon class="stripe-navy" points="196,460 214,460 254,300 246,268" fill="var(--navy)"/>
    <polygon class="stripe-sky" points="300,0 316,0 266,230 326,460 310,460 250,230" fill="var(--sky)"/>

    <!-- right tech texture field with chevron -->
    <polygon class="stripe-navy" points="930,0 960,0 1050,240 1025,240" fill="var(--navy)"/>
    <polygon class="texture-right" role="img" aria-label="Blue circuit-board texture"
      points="978,0 1100,0 1100,460 968,460 1068,240" fill="url(#circuit-tone)"/>
    <polygon class="stripe-sky" points="965,0 978,0 1068,240 968,460 955,460 1055,240" fill="var(--sky)"/>

    <!-- services list -->
    <g class="services">
      <text class="service-heading" x="420" y="262" text-anchor="end">OUR</text>
      <text class="service-heading" x="420" y="290" text-anchor="end">SERVICE</text>
      <rect x="432" y="180" width="3" height="132" fill="var(--sky)"/>
      <text class="service-item" x="444" y="196">IT Support</text>
      <text class="service-item" x="444" y="218">Telecoms and Internet,</text>
      <text class="service-item" x="444" y="240">Cloud Computing,</text>
      <text class="service-item" x="444" y="262">Cyber Security,</text>
      <text class="service-item" x="444" y="284">Networking Design and Installation,</text>
      <text class="service-item" x="444" y="306">Printers and Copiers,</text>
    </g>

    <!-- brand mark: plain ring and name -->
    <g class="brand">
      <circle class="brand-ring" cx="870" cy="150" r="85"/>
      <text class="brand-name" x="870" y="300" text-anchor="middle">BRIGHTWIRE TECH</text>
    </g>

    <!-- contact band -->
    <g class="contact-band">
      <polygon points="300,340 1000,340 996,346 302,346" fill="var(--sky)"/>
      <polygon points="310,352 990,352 965,410 330,410" fill="var(--navy)"/>
      <text class="phone" x="360" y="392">0330 555 0192</text>
      <text class="website" x="950" y="388" text-anchor="end">www.brightwiretech.com</text>
    </g>
  </svg>
</main>
</body>
</html>
```